Business Card Design

Electric home brewing equipment. Custom and catalog items. Most products are made by or for my company, so name is on most everything. Travel to conventions, to meet with home brewers. Trying to create a professional, but since primarily home brewers, fun image. New logo attached, with this new logo I'm redoing most materials. I'm trying to create a single brand under this logo.
Bolt icon on card, does not have to be directly over text as in logo file, but can be used similar to my example.

Website address is http://www.voltkettleworks.com (this is a must add).

New video intro to be added to video productions here: http://clipvault.example/k7Rm2xQwLp

Target Market(s)

Home brewers, predominantly male, ages 21 - 55, tend to be looking for the hot new thing.

Industry/Entity Type

Business

Contact Information for Business Card

Details as included on file. Layout I've attached is approximately what I'm looking for. Single and Double sided cards options welcome.

Card info should include:
2 cards: Derek Holm and Mona Holm
Both: Owners
Email: derek@voltkettleworks.com and mona@voltkettleworks.com
Both phone: 888-472-0635
Both address: Lakeview, Texas 77512
Website: voltkettleworks.com

Requirements
Must have
• Use both parts of the logo, not necessarily together as design should infer.

```html
<!DOCTYPE html>
<html lang="en">
<head>
<meta charset="utf-8">
<title>Volt Kettle Works – Business Card</title>
<link href="https://fonts.googleapis.com/css2?family=Open+Sans:wght@400;700;800&display=swap" rel="stylesheet">
<style>
  :root {
    --bg: #e9e6e1;
    --card-black: #0b0b0b;
    --card-white: #ffffff;
    --brand-yellow: #fbbd1a;
    --art-mid: #3a3428;
    --ink-white: #ffffff;
    --ink-black: #111111;
  }
  html, body {
    margin: 0;
    width: 1200px;
    height: 1019px;
    overflow: hidden;
    background: var(--bg);
    font-family: "Open Sans", Arial, sans-serif;
  }
  .canvas {
    position: relative;
    width: 1200px;
    height: 1019px;
  }
  .card {
    position: absolute;
    left: 220px;
    width: 760px;
    height: 434px;
    box-shadow: 0 6px 18px rgba(0,0,0,0.22);
    overflow: hidden;
  }
  .card-front { top: 45px; background: var(--card-black); }
  .card-back  { top: 540px; background: var(--card-white); }

  .gauge-art {
    position: absolute;
    left: 0;
    right: 0;
    bottom: 0;
    height: 250px;
    background: radial-gradient(ellipse at 55% 100%, var(--brand-yellow) 0%, var(--art-mid) 45%, var(--card-black) 80%);
  }

  .contact { position: absolute; top: 40px; color: var(--ink-white); font-size: 19px; line-height: 1.4; white-space: nowrap; }
  .contact .accent { color: var(--brand-yellow); font-weight: 700; }
  .contact-address { left: 40px; }
  .contact-reach { left: 285px; }
  .contact-person { right: 40px; text-align: right; }
  .contact-person .name { color: var(--brand-yellow); font-weight: 800; font-size: 24px; line-height: 1.2; }
  .contact-person .role { font-weight: 800; font-size: 20px; }

  .brand {
    position: absolute;
    inset: 0;
    display: flex;
    align-items: center;
    justify-content: center;
    gap: 26px;
  }
  .brand-dot {
    width: 86px; height: 86px;
    border-radius: 50%;
    background: var(--brand-yellow);
  }
  .brand-name {
    font-weight: 800;
    font-size: 56px;
    letter-spacing: -1px;
    color: var(--ink-black);
  }
</style>
</head>
<body>
<main class="canvas">
  <section class="card card-front">
    <div class="gauge-art" role="img" aria-label="Gauge illustration: white dial arc with a yellow needle"></div>
    <div class="contact contact-address">
      <div>Lakeview, Texas 77512</div>
      <div class="accent">voltkettleworks.com</div>
    </div>
    <div class="contact contact-reach">
      <div>phone: 888.472.0635</div>
      <div>derek@voltkettleworks.com</div>
    </div>
    <div class="contact contact-person">
      <div class="name">Derek Holm</div>
      <div class="role">owner</div>
    </div>
  </section>

  <section class="card card-back">
    <div class="brand">
      <span class="brand-dot"></span>
      <span class="brand-name">Volt Kettle Works</span>
    </div>
  </section>
</main>
</body>
</html>
```